Comets Business Card Design Project

Create a standard format for letterhead and business cards. I know I can just get the layout with an example name on it, then add the names, titles and address that we want to it and give that to a printer so that the graphics are much better. Organization Mission Statement: Providing a professionally organized, structured, and supportive environment with quality development and professional coaching to inspire our student athletes, and assist them in fulfilling their dreams of achievement in academic excellence, high level competition and playing collegiate softball. Girl's Elite Fastpitch Softball

Check web site: www.brookvalediamondcomets.org
Updates

Sorry I didn't get the URL and files out when I started the project. Logo examples, mission, vision, etc. are posted now. And the URL to the web site is www.brookvalediamondcomets.org.

I'm very interested in an original creative design that is professional yet relevant to a sports team and for coaches.

Target Market(s)

college recuriters, industry product suppliers, parents, coaches, tournament directors

Industry/Entity Type

Environment

Requirements
Must have
• Use one of two logos; include the web site URL and a general mailbox for inquires. Includes Name, title, email and phone number
Nice to have
• Some color variations or background. Maybe a mission statement on the back. Maybe a QR code to the web site.

```html
<!DOCTYPE html>
<html lang="en">
<head>
<meta charset="utf-8">
<title>Brookvale Comets – Business Card</title>
<link rel="stylesheet" href="https://fonts.googleapis.com/css2?family=Quicksand:wght@400;500;700&display=swap">
<style>
  :root {
    --page-bg: #2a2a2a;
    --dirt-dark: #3a1f12;
    --dirt-mid: #7a4a2e;
    --dirt-light: #9a6646;
    --ball-tone: #8c8f3c;
    --brand-red: #e3203f;
    --panel-white: rgba(255, 255, 255, 0.2);
    --text-white: #ffffff;
    --text-soft: #f1ece8;
  }
  * { margin: 0; padding: 0; box-sizing: border-box; }
  html, body {
    width: 1200px;
    height: 1000px;
    overflow: hidden;
    background: var(--page-bg);
    font-family: "Quicksand", sans-serif;
  }
  .business-card {
    position: absolute;
    left: 80px;
    top: 216px;
    width: 1040px;
    height: 568px;
    overflow: hidden;
  }
  .card-photo {
    position: absolute;
    inset: 0;
    background:
      radial-gradient(circle at 866px 300px, rgba(140,143,60,0.75) 0, rgba(140,143,60,0.55) 90px, rgba(122,74,46,0) 190px),
      radial-gradient(ellipse at 45% 35%, var(--dirt-light) 0%, var(--dirt-mid) 45%, var(--dirt-dark) 100%);
  }
  .team-name {
    position: absolute;
    left: 38px;
    top: 42px;
    display: flex;
    align-items: center;
    gap: 14px;
    color: var(--brand-red);
    font-weight: 700;
    font-size: 50px;
    line-height: 1;
  }
  .team-dot {
    width: 26px;
    height: 26px;
    border-radius: 50%;
    background: var(--brand-red);
  }
  .contact-panel {
    position: absolute;
    left: 0;
    top: 285px;
    width: 434px;
    height: 225px;
    background: var(--panel-white);
    color: var(--text-white);
  }
  .person-heading {
    position: absolute;
    left: 26px;
    top: 22px;
    display: inline-flex;
    flex-direction: column;
    align-items: flex-end;
  }
  .person-name {
    font-size: 28px;
    font-weight: 500;
    letter-spacing: 0.6px;
    line-height: 1.1;
  }
  .person-title {
    margin-top: 1px;
    font-size: 12.5px;
    font-weight: 500;
    letter-spacing: 0.4px;
    line-height: 1;
    text-transform: uppercase;
  }
  .contact-list {
    position: absolute;
    left: 43px;
    top: 106px;
    list-style: none;
    font-size: 13px;
    line-height: 16px;
    color: var(--text-soft);
  }
  .contact-list li { margin-bottom: 15px; }
  .contact-list strong { font-weight: 700; color: var(--text-white); }
  .site-url {
    position: absolute;
    right: 16px;
    bottom: 12px;
    font-size: 16px;
    font-weight: 500;
    letter-spacing: 4.6px;
    color: var(--text-white);
    text-transform: uppercase;
  }
</style>
</head>
<body>
  <main class="business-card">
    <div class="card-photo" role="img" aria-label="Close-up photo of infield dirt with a worn yellow softball resting on the right"></div>

    <div class="team-name">
      <span class="team-dot"></span>
      <span>Brookvale Comets</span>
    </div>

    <section class="contact-panel">
      <div class="person-heading">
        <h1 class="person-name">Dana Whitfield</h1>
        <p class="person-title">Head Coach</p>
      </div>
      <ul class="contact-list">
        <li><strong>Phone:</strong> 555 204 773</li>
        <li><strong>Address:</strong> 412 Maple Avenue Brookvale, CA 90210</li>
        <li><strong>Email:</strong> info@brookvalecomets.org</li>
      </ul>
    </section>

    <p class="site-url">www.brookvalediamondcomets.org</p>
  </main>
</body>
</html>
```